A website for Varnholt Limited

We need a new and modern website for our company. We are engineering consultants and contractors (EPC) in the oil and gas industry and building services industry.
What we do:
Engineering, procurement, construction
Automation (safety and process)
Non-destructive testing
Training
We have an existing website and the content can be referred from there since we are remaking the website
For more information visit Varnholt Limited Kenya

Coding

Number of Pages Required

1 page

```html
<!DOCTYPE html>
<html lang="en">
<head>
<meta charset="utf-8">
<title>Varnholt Limited</title>
<link href="https://fonts.googleapis.com/css2?family=Josefin+Sans:wght@400;600;700&family=Roboto+Condensed:wght@400;700&display=swap" rel="stylesheet">
<style>
:root{
  --orange:#f0873f;
  --orange-deep:#e5673a;
  --orange-soft:#f6b160;
  --ink:#111111;
  --white:#ffffff;
  --grey:#dedede;
  --blue:#2b3f9e;
  --sky:#9fc3dd;
}
*{box-sizing:border-box;margin:0;padding:0}
html,body{width:1200px;height:2834px;overflow:hidden}
body{position:relative;background:var(--white);font-family:'Josefin Sans',sans-serif;color:var(--ink)}
.abs{position:absolute}
.brand{display:flex;align-items:center;gap:10px;font-family:'Josefin Sans',sans-serif;font-weight:600;color:var(--white);text-transform:uppercase;letter-spacing:1px}
.brand .mark{border-radius:50%;border:3px solid currentColor}
.btn{display:flex;align-items:center;justify-content:center;border-radius:26px;color:var(--white);font-weight:600;font-size:22px;background:linear-gradient(90deg,var(--orange-deep),var(--orange-soft))}

/* hero */
.hero{left:0;top:0;width:1200px;height:555px;background:linear-gradient(100deg,#233a95 0%,#5a4fa6 30%,#b77ab3 60%,#f2a68a 85%,#e88a6a 100%)}
.hero-plant{left:0;top:300px;width:1200px;height:255px;background:linear-gradient(180deg,rgba(40,35,60,0) 0%,rgba(60,45,60,.55) 55%,rgba(120,80,60,.7) 100%)}
.hero .brand{left:108px;top:14px;font-size:21px}
.menu{left:1053px;top:32px;width:32px}
.menu span{display:block;height:3px;background:var(--white);margin-bottom:8px}
.hero h1{left:123px;top:150px;font-size:50px;line-height:58px;font-weight:600;color:var(--white);letter-spacing:1px}
.hero p{left:124px;top:275px;width:440px;font-size:14px;line-height:21px;color:var(--white)}
.hero .btn{left:126px;top:374px;width:160px;height:46px}

/* section headings */
.heading{font-size:46px;font-weight:700;display:flex;align-items:center}
.heading .ring{width:68px;height:68px;border:3px solid var(--orange);border-radius:50%;border-right-color:transparent;transform:rotate(-30deg);margin-right:-28px;flex:none}

.what{left:0;top:612px;width:1200px;justify-content:center}
.card{top:705px;height:299px;background:var(--orange-soft)}
.card.active{background:var(--orange-deep)}
.card.fade{background:var(--sky);opacity:.7}
.card .photo{position:absolute;left:10px;top:10px;right:10px;height:198px}
.card .label{position:absolute;left:0;right:0;top:240px;text-align:center;color:var(--white);font-size:27px;font-weight:700;letter-spacing:1px}
.arrow{width:44px;height:44px;border-radius:50%;background:var(--orange-deep);border:2px solid var(--white)}
.arrow svg{display:block}
.what-more{left:505px;top:1050px;width:159px;height:46px}

/* about */
.about-band{left:0;top:1246px;width:1200px;height:447px;background:linear-gradient(90deg,#f3894a,#f39a5c 60%,#f08a4e)}
.about-photo{left:110px;top:1181px;width:446px;height:465px;background:linear-gradient(160deg,#e6e8ec,#b8bfc8 50%,#e9a070 100%)}
.about-head{left:609px;top:1275px;color:var(--white)}
.about-head .ring{border-color:var(--white);border-right-color:transparent}
.about h3{left:609px;top:1358px;font-size:25px;font-weight:600;color:var(--white)}
.about p{left:609px;top:1405px;width:485px;font-size:15px;line-height:20.5px;color:var(--white)}
.about .btn{left:607px;top:1575px;width:159px;height:46px}

/* why */
.why{left:0;top:1772px;width:1200px;justify-content:center}
.tabs{left:249px;top:1888px;width:702px;height:54px;border:2px solid var(--grey);border-radius:4px}
.tab{top:1881px;height:69px;display:flex;align-items:center;justify-content:center;font-size:26px;font-weight:600}
.tab.on{background:var(--orange);color:var(--white)}
.hex{top:1995px;width:206px;height:230px}
.hex-label{top:2252px;width:206px;text-align:center;font-size:26px;font-weight:600}

/* footer */
.footer{left:0;top:2372px;width:1200px;height:462px;background:#000}
.footer .brand{left:0;top:2440px;width:1200px;justify-content:center;font-size:28px}
.contact{display:flex;gap:14px;color:var(--white);font-family:'Roboto Condensed',sans-serif}
.contact .ico{width:38px;height:38px;border:1px solid #777;border-radius:50%;display:flex;align-items:center;justify-content:center;flex:none}
.contact small{display:block;font-size:12px;font-weight:700;margin-top:2px}
.contact span{display:block;font-size:15px;line-height:23px;margin-top:4px}
.nav{left:0;top:2688px;width:1200px;height:68px;background:var(--orange);display:flex;justify-content:center;align-items:center;gap:21px;color:var(--white);font-size:16px;font-weight:600}
.copy{left:0;top:2781px;width:1200px;text-align:center;color:var(--white);font-size:18px}
</style>
</head>
<body>

<header class="abs hero">
  <div class="abs hero-plant" role="img" aria-label="Refinery towers and storage spheres at dusk"></div>
  <div class="abs brand"><span class="mark" style="width:60px;height:60px"></span>Varnholt Limited</div>
  <div class="abs menu"><span></span><span></span><span></span></div>
  <h1 class="abs">WELCOME TO<br>VARNHOLT LIMITED</h1>
  <p class="abs">Lorem ipsum dolor sit amet, consectetur adipiscing elit, sed do eiusmod tempor incididunt ut labore et dolore magna aliqua. Ut enim ad minim veniam, quis nostrud exercitation ullamco laboris nisi ut aliquip ex ea commodo consequat.</p>
  <a class="abs btn">Get Started</a>
</header>

<h2 class="abs heading what"><span class="ring"></span>What we do</h2>

<div class="abs card fade" style="left:0;width:88px"><div class="photo" style="left:0;background:linear-gradient(135deg,#cfe0ee,#8fb5d3)" role="img" aria-label="Service photo"></div><div class="label" style="text-align:left;left:-6px">TIVE</div></div>
<div class="abs card" style="left:106px;width:318px"><div class="photo" role="img" aria-label="Engineers reviewing technical plans on a desk" style="background:linear-gradient(135deg,#e9ecf2,#b9c0cc)"></div><div class="label">ENGINEERING</div></div>
<div class="abs card active" style="left:440px;width:317px"><div class="photo" role="img" aria-label="Worker standing among shipping containers" style="background:linear-gradient(180deg,#5c9ad8 0%,#8dbbe0 45%,#9a9d9f 75%,#b8b4ad 100%)"></div><div class="label">PROCUREMENT</div></div>
<div class="abs card" style="left:773px;width:318px"><div class="photo" role="img" aria-label="Engineers on a construction site" style="background:linear-gradient(180deg,#d9c6a6 0%,#9c8a72 55%,#6a5d50 100%)"></div><div class="label">CONSTRUCTION</div></div>
<div class="abs card fade" style="left:1108px;width:92px"><div class="photo" style="right:0;background:linear-gradient(135deg,#cfe0ee,#8fb5d3)" role="img" aria-label="Service photo"></div><div class="label" style="text-align:left;left:52px">AU</div></div>

<div class="abs arrow" style="left:25px;top:823px"><svg width="40" height="40" viewBox="0 0 40 40"><circle cx="20" cy="20" r="13" fill="none" stroke="#fff" stroke-width="2"/><path d="M23 13 L15 20 L23 27 Z" fill="none" stroke="#fff" stroke-width="2" stroke-linejoin="round"/></svg></div>
<div class="abs arrow" style="left:1128px;top:823px"><svg width="40" height="40" viewBox="0 0 40 40"><circle cx="20" cy="20" r="13" fill="none" stroke="#fff" stroke-width="2"/><path d="M17 13 L25 20 L17 27 Z" fill="none" stroke="#fff" stroke-width="2" stroke-linejoin="round"/></svg></div>
<a class="abs btn what-more">See More</a>

<section class="about">
  <div class="abs about-band" role="img" aria-label="Orange-toned row of pipeline valves"></div>
  <div class="abs about-photo" role="img" aria-label="Engineer in orange coveralls inspecting a gas plant"></div>
  <h2 class="abs heading about-head"><span class="ring"></span>About Us</h2>
  <h3 class="abs">Who We Are</h3>
  <p class="abs">Varnholt undertakes Design, Supply, Installation and Commissioning of LPG and Petroleum systems including LPG Reticulated Systems (piped gas). We also do LPG tank revalidation and recertification. Our clients include: Oil companies (both multinationals and local), government agencies, manufacturing companies, agricultural institutions, and the building services industry.</p>
  <a class="abs btn">See More</a>
</section>

<h2 class="abs heading why"><span class="ring"></span>Why Choose Us</h2>
<div class="abs tabs"></div>
<div class="abs tab" style="left:249px;width:234px">Our Services</div>
<div class="abs tab on" style="left:483px;width:242px">Our Products</div>
<div class="abs tab" style="left:725px;width:226px">Our Projects</div>

<svg class="abs hex" style="left:110px" viewBox="0 0 206 230"><polygon points="103,2 204,58 204,172 103,228 2,172 2,58" fill="#fff" stroke="#f0873f" stroke-width="4"/><polygon points="103,12 195,63 195,167 103,218 11,167 11,63" fill="#dedede"/>
<g fill="none" stroke="#111" stroke-width="3" stroke-linejoin="round"><rect x="76" y="65" width="54" height="110" rx="10"/><rect x="88" y="52" width="30" height="14"/><line x1="76" y1="90" x2="130" y2="90"/><line x1="76" y1="155" x2="130" y2="155"/><path d="M103 108 C90 122 92 140 103 140 C114 140 116 124 103 108 Z"/></g></svg>
<div class="abs hex-label" style="left:110px">LPG</div>

<svg class="abs hex" style="left:367px" viewBox="0 0 206 230"><polygon points="103,2 204,58 204,172 103,228 2,172 2,58" fill="#fff" stroke="#f0873f" stroke-width="4"/><polygon points="103,12 195,63 195,167 103,218 11,167 11,63" fill="#000"/>
<g fill="none" stroke="#f0873f" stroke-width="3" stroke-linejoin="round"><path d="M45 72 L150 72 L160 85 L150 98 L45 98 Z"/><path d="M88 98 L70 170 M112 98 L130 170 M78 135 L122 135 M74 152 L126 152"/><line x1="50" y1="170" x2="165" y2="170"/><circle cx="60" cy="135" r="10"/><line x1="60" y1="98" x2="60" y2="125"/><line x1="150" y1="98" x2="150" y2="150"/></g></svg>
<div class="abs hex-label" style="left:367px">Petroleum</div>

<svg class="abs hex" style="left:624px" viewBox="0 0 206 230"><polygon points="103,2 204,58 204,172 103,228 2,172 2,58" fill="#fff" stroke="#f0873f" stroke-width="4"/><polygon points="103,12 195,63 195,167 103,218 11,167 11,63" fill="#dedede"/>
<g fill="none" stroke="#111" stroke-width="3"><circle cx="82" cy="135" r="22" stroke-dasharray="8 4" stroke-width="10"/><circle cx="82" cy="135" r="10"/><circle cx="128" cy="80" r="15" stroke-dasharray="6 3" stroke-width="8"/><circle cx="128" cy="80" r="6"/><circle cx="140" cy="122" r="13" stroke-dasharray="6 3" stroke-width="7"/><circle cx="140" cy="122" r="5"/><path d="M50 110 A45 45 0 0 1 90 88"/></g></svg>
<div class="abs hex-label" style="left:624px">Automation</div>

<svg class="abs hex" style="left:881px" viewBox="0 0 206 230"><polygon points="103,2 204,58 204,172 103,228 2,172 2,58" fill="#fff" stroke="#f0873f" stroke-width="4"/><polygon points="103,12 195,63 195,167 103,218 11,167 11,63" fill="#dedede"/>
<g fill="none" stroke="#111" stroke-width="3" stroke-linejoin="round"><path d="M52 85 L66 85 L66 72 L78 72 L78 150 L66 150 L66 138 L52 138 Z"/><path d="M78 105 L100 105 L100 118 L78 118"/><path d="M105 96 L130 110 L105 124"/><path d="M118 85 C165 70 180 110 160 125 C150 140 125 135 118 125"/><circle cx="150" cy="110" r="9"/></g></svg>
<div class="abs hex-label" style="left:881px">Fire Fighting</div>

<footer class="abs footer"></footer>
<div class="abs brand" style="left:0;top:2432px;width:1200px;justify-content:center;font-size:28px"><span class="mark" style="width:96px;height:96px;border-width:4px"></span>Varnholt Limited</div>

<div class="abs contact" style="left:123px;top:2603px">
  <div class="ico"><svg width="18" height="14" viewBox="0 0 18 14"><rect x="1" y="1" width="16" height="12" rx="2" fill="none" stroke="#fff" stroke-width="1.6"/><path d="M1 2 L9 8 L17 2" fill="none" stroke="#fff" stroke-width="1.6"/></svg></div>
  <div><small>EMAIL</small><span>info@varnholtltd.com</span></div>
</div>
<div class="abs contact" style="left:454px;top:2603px">
  <div class="ico"><svg width="14" height="18" viewBox="0 0 14 18"><path d="M7 17 C2 10 1 8 1 6 A6 6 0 0 1 13 6 C13 8 12 10 7 17 Z" fill="#fff"/><circle cx="7" cy="6" r="2" fill="#000"/></svg></div>
  <div><small>OUR LOCATION</small><span>19 Nemo enim ipsam voluptatem<br>quia voluptas sit</span></div>
</div>
<div class="abs contact" style="left:813px;top:2603px">
  <div class="ico"><svg width="16" height="16" viewBox="0 0 16 16"><path d="M3 1 L6 1 L7 5 L5 6 C6 9 7 10 10 11 L11 9 L15 10 L15 13 C15 14 14 15 13 15 C6 15 1 10 1 3 C1 2 2 1 3 1 Z" fill="#fff"/></svg></div>
  <div><small>PHONE NUMBER</small><span>+1 888-888-8888</span></div>
</div>

<nav class="abs nav"><span>Home</span><span>About Us</span><span>Services</span><span>Products</span><span style="margin-left:-10px">our Projects</span><span>our Clients</span><span>Where We Operate</span><span style="margin-left:-5px">our Partners</span><span>Contacts</span></nav>
<p class="abs copy">Copyright © 2023 Varnholt - All Rights Reserved.</p>

</body>
</html>
```